Somaliland Vs Sealand

We are hosting an international football match between Somaliland and Sealand, to celebrate the 23rd independence anniversary of Somaliland. I need a flyer to promote the game. The Match will be taking place on Saturday the 17/05/2014, kick off is at 2pm. The Venue will be, Marwick Park Stadium, Tottenham, London, N19 4QB.
Enclosed, I have attached files of each countries national football emblem and their national flags colours.
I have enclosed few flyers for your attention of possible designs to take lead from.

I would like each countries flags to appear in circle shapes if possible and somehow include small images of the national flags, perhaps on the edges of the flyer.
£5 entry for tickets, all donations for charity.

Charity

```html
<!DOCTYPE html>
<html lang="en">
<head>
<meta charset="utf-8">
<title>Sealand vs Somaliland – Match Flyer</title>
<link rel="stylesheet" href="https://fonts.googleapis.com/css2?family=Oswald:wght@300;400;600;700&family=Roboto+Condensed:wght@400;700&display=swap">
<style>
  :root {
    --page-bg: #e4e6e8;
    --poster-black: #050607;
    --night-blue: #0b1a33;
    --stand-blue: #12315a;
    --pitch-green: #6fae1f;
    --pitch-bright: #c8e43a;
    --lime: #c6e02c;
    --kick-green: #7cc42a;
    --flag-red: #d7232e;
    --flag-white: #f3f3f3;
    --flag-green: #1f8b3b;
    --silver-light: #f4f6f8;
    --silver-dark: #8e969e;
    --label-white: #e8ecef;
  }
  * { margin: 0; padding: 0; box-sizing: border-box; }
  html, body { width: 1200px; height: 861px; overflow: hidden; }
  body { background: var(--page-bg); position: relative; }

  .poster {
    position: absolute; left: 385px; top: 30px;
    width: 430px; height: 800px;
    background: var(--poster-black);
    overflow: hidden;
    box-shadow: 0 6px 24px rgba(0,0,0,.25);
  }

  .stadium-scene {
    position: absolute; left: 0; top: 160px; width: 430px; height: 400px;
    background:
      radial-gradient(ellipse 80% 40% at 50% 82%, var(--pitch-bright) 0%, var(--pitch-green) 45%, rgba(20,60,10,0) 75%),
      linear-gradient(180deg, var(--night-blue) 0%, var(--stand-blue) 45%, #1b3d2a 68%, #163d12 100%);
  }

  .flag-banner {
    position: absolute; left: 0; top: 0; width: 430px; height: 230px;
    background: linear-gradient(160deg, var(--flag-red) 0%, #e86a6a 20%, var(--flag-white) 45%, #dcdcdc 62%, var(--flag-green) 88%);
    border-radius: 0 0 50% 50% / 0 0 60px 60px;
  }
  .flag-banner::after {
    content: ""; position: absolute; inset: 0;
    border-radius: inherit;
    border-bottom: 5px solid #0d1420;
  }

  .match-ball {
    position: absolute; left: 174px; top: 160px; width: 82px; height: 82px;
    border-radius: 50%;
    background: radial-gradient(circle at 40% 35%, #ffffff 0%, #cfd3d6 60%, #6c7378 100%);
  }

  .crowd {
    position: absolute; left: 0; top: 500px; width: 430px; height: 150px;
    background: linear-gradient(180deg, rgba(5,6,7,0) 0%, rgba(5,6,7,.85) 40%, var(--poster-black) 100%);
  }

  .crest-label {
    position: absolute;
    font-family: "Roboto Condensed", sans-serif; font-weight: 400;
    font-size: 9px; line-height: 1.25; color: var(--label-white);
    text-align: center;
  }
  .crest-label .mark {
    display: block; margin: 0 auto 6px; width: 14px; height: 14px;
    border-radius: 50%; background: var(--label-white);
  }
  .crest-label--home { left: 12px; top: 298px; width: 100px; }
  .crest-label--away { left: 352px; top: 380px; width: 72px; }

  .fixture {
    position: absolute; white-space: nowrap;
    font-family: "Oswald", sans-serif; font-weight: 600;
    text-transform: uppercase; letter-spacing: 1px; line-height: 1;
    background: linear-gradient(180deg, var(--silver-light) 0%, #c9ced3 48%, var(--silver-dark) 52%, #dfe3e6 100%);
    -webkit-background-clip: text; background-clip: text; color: transparent;
  }
  .fixture--home { left: 114px; top: 272px; font-size: 44px; }
  .fixture--home .vs {
    margin-left: 12px;
    background: linear-gradient(180deg, #e9f1fb 0%, #7fa8d8 55%, #4b79b8 100%);
    -webkit-background-clip: text; background-clip: text; color: transparent;
  }
  .fixture--away { left: 110px; top: 332px; font-size: 44px; }

  .details { position: absolute; left: 56px; top: 596px; width: 350px; }
  .match-date {
    font-family: "Oswald", sans-serif; font-weight: 300;
    font-size: 28px; letter-spacing: 3.5px; color: var(--lime);
    text-transform: uppercase; line-height: 1.2;
  }
  .kick-off {
    font-family: "Oswald", sans-serif; font-weight: 600;
    font-size: 42px; color: var(--kick-green); text-transform: uppercase;
    margin-top: 0; line-height: 1.1;
  }
  .venue {
    font-family: "Roboto Condensed", sans-serif; font-weight: 700;
    font-size: 12.5px; color: var(--lime); text-transform: uppercase;
    margin-top: 6px; white-space: nowrap;
  }
  .entry {
    font-family: "Roboto Condensed", sans-serif; font-weight: 400;
    font-size: 18px; color: var(--kick-green); margin-top: 30px; white-space: nowrap;
  }
</style>
</head>
<body>
  <main class="poster">
    <div class="stadium-scene" role="img" aria-label="Floodlit football stadium with crowd in the stands and a green pitch"></div>
    <div class="flag-banner" role="img" aria-label="Waving Sealand and Somaliland national flags"></div>
    <div class="match-ball" role="img" aria-label="Football"></div>
    <div class="crowd" role="img" aria-label="Silhouettes of cheering fans waving flags"></div>

    <div class="crest-label crest-label--home"><span class="mark"></span>Sealand Island Football Club</div>
    <div class="crest-label crest-label--away"><span class="mark"></span>Horn Coast Football Union</div>

    <h1>
      <span class="fixture fixture--home">Sealand<span class="vs">vs</span></span>
      <span class="fixture fixture--away">Somaliland</span>
    </h1>

    <section class="details">
      <p class="match-date">Saturday&nbsp; 17/05/2014</p>
      <p class="kick-off">Kick off at 2pm</p>
      <p class="venue">Marwick Park Stadium, Tottenham, London, N19 4QB</p>
      <p class="entry">£5 Entry for tickets, All donations for charity</p>
    </section>
  </main>
</body>
</html>
```